Flyer Design

We are a property company and need attractive flyers that will grab peoples attention. We want them to be bold but simple and not too busy. I attach a draft and also our logo. We will print in A5 size.
Thank you & I look forward to receiving designs.

It Company

```html
<!DOCTYPE html>
<html lang="en">
<head>
<meta charset="utf-8">
<title>Orla Developments – Subdivision Flyer</title>
<link rel="stylesheet" href="https://fonts.googleapis.com/css2?family=Roboto+Condensed:wght@700&family=Source+Sans+3:wght@400;600;700&display=swap">
<style>
  :root {
    --backdrop: #2a1c15;
    --band-red: #b63a32;
    --cream: #fdf0c6;
    --wood-light: #ddd5c8;
    --wood-mid: #cfc4b4;
    --brand-brown: #6b3a22;
    --text-brown: #4c2a22;
    --white: #ffffff;
  }
  * { margin: 0; padding: 0; box-sizing: border-box; }
  html, body {
    width: 1200px; height: 964px; overflow: hidden;
    background: var(--backdrop);
  }
  .flyer {
    position: absolute; left: 40px; top: 86px;
    width: 1120px; height: 792px;
    display: flex; flex-direction: column;
    box-shadow: 0 6px 24px rgba(0,0,0,.5);
  }
  .headline-band {
    height: 154px; background: var(--band-red);
    display: flex; align-items: center; justify-content: center;
    text-align: center;
  }
  .headline {
    font-family: "Roboto Condensed", "Arial Narrow", sans-serif;
    font-weight: 700; font-size: 46px; line-height: 58px;
    color: var(--cream); letter-spacing: .5px;
    text-shadow: 2px 2px 3px rgba(60,10,5,.55);
  }
  .feature-panel {
    position: relative; height: 538px;
    display: flex; flex-direction: column; align-items: center;
  }
  .wood-surface {
    position: absolute; inset: 0;
    background: linear-gradient(100deg, var(--wood-mid) 0%, var(--wood-light) 40%, #e4ddd2 70%, var(--wood-mid) 100%);
  }
  .brand {
    position: relative; margin-top: 120px;
    display: flex; flex-direction: column; align-items: center; gap: 36px;
  }
  .brand-square {
    width: 90px; height: 90px; background: var(--brand-brown);
  }
  .brand-name {
    font-family: "Source Sans 3", "Myriad Pro", sans-serif;
    font-weight: 600; font-size: 86px; line-height: 1;
    color: var(--brand-brown); letter-spacing: 3px;
  }
  .question {
    position: relative; margin-top: 64px;
    font-family: "Roboto Condensed", "Arial Narrow", sans-serif;
    font-weight: 700; font-size: 36px;
    color: var(--text-brown); letter-spacing: .5px;
  }
  .service-line {
    position: relative; margin-top: 4px;
    font-family: "Source Sans 3", "Myriad Pro", sans-serif;
    font-weight: 600; font-size: 25px;
    color: var(--text-brown);
  }
  .contact-band {
    height: 100px; background: var(--band-red);
    display: flex; align-items: center; justify-content: center;
    text-align: center;
    font-family: "Source Sans 3", "Myriad Pro", sans-serif;
    font-size: 21px; line-height: 29px; color: var(--white);
  }
  .contact-band strong { font-weight: 700; }
</style>
</head>
<body>
  <main class="flyer">
    <header class="headline-band">
      <h1 class="headline">Are you a homeowner looking for financial<br>freedom while been able to keep your own home?</h1>
    </header>

    <section class="feature-panel">
      <div class="wood-surface" role="img" aria-label="Light oak wood grain texture"></div>
      <div class="brand">
        <span class="brand-square"></span>
        <p class="brand-name">Orla Developments</p>
      </div>
      <h2 class="question">ARE YOU STRUGGLING TO PAY YOUR MORTGAGE?</h2>
      <p class="service-line">ORLA specialise in subdivisions including finance and management</p>
    </section>

    <footer class="contact-band">
      <p><strong>Call 021 555 0142</strong>&nbsp; or &nbsp;<strong>email info@orlasubdivisions.com</strong> for more information or to find out if<br>your property is suitable for subdivision in Auckland. &nbsp; <strong>www.OrlaSubDivisions.com</strong></p>
    </footer>
  </main>
</body>
</html>
```